I just need to get that same logo on the business card but with different word. “Marlow Tow and Lease”

Name: Dale K
Number: 4752869014
Email: marlowtow@fennmail.test

On the back, can we di just the logo and marlow tow and lease around it.

If possible a black card with the gold storefront type font that you used before, would be amazing. I attached the original logo just in case.

Target Market(s)

Roadside assistance

Industry/Entity Type

Repair/ roadside

Contact Information for Business Card

Name, email, phone number

Requirements
Must have
• Everything in description
Nice to have
• Nice big logo

```html
<!DOCTYPE html>
<html lang="en">
<head>
<meta charset="utf-8">
<title>Marlow Tow and Lease — Business Card</title>
<link rel="stylesheet" href="https://fonts.googleapis.com/css2?family=Cinzel:wght@500&family=Inter:wght@400&display=swap">
<style>
  :root {
    --backdrop: #141516;
    --card: #1f2021;
    --card-edge: #2a2b2c;
    --gold: #c9982f;
    --gold-light: #d8ab45;
  }
  * { box-sizing: border-box; margin: 0; padding: 0; }
  html, body {
    width: 1200px;
    height: 1200px;
    overflow: hidden;
    background: var(--backdrop);
  }
  .canvas {
    width: 1200px;
    height: 1200px;
    display: flex;
    flex-direction: column;
    align-items: center;
    justify-content: center;
    gap: 48px;
  }
  .card {
    position: relative;
    width: 840px;
    height: 480px;
    background: var(--card);
    border: 1px solid var(--card-edge);
    color: var(--gold);
  }

  /* Front: brand mark area with the company line beneath */
  .card--front {
    display: flex;
    flex-direction: column;
    align-items: center;
    justify-content: center;
    gap: 44px;
  }
  .brand-mark {
    display: flex;
    align-items: center;
    gap: 18px;
  }
  .brand-mark__square {
    width: 34px;
    height: 34px;
    background: var(--gold);
  }
  .brand-mark__name {
    font-family: "Cinzel", serif;
    font-weight: 500;
    font-size: 40px;
    letter-spacing: 0.04em;
    color: var(--gold);
  }
  .company-line {
    font-family: "Cinzel", serif;
    font-weight: 500;
    font-size: 27px;
    letter-spacing: 0.06em;
    color: var(--gold);
  }

  /* Back: name, contacts, brand mark corner */
  .holder-name {
    position: absolute;
    top: 58px;
    left: 64px;
    font-family: "Cinzel", serif;
    font-weight: 500;
    font-size: 28px;
    letter-spacing: 0.04em;
  }
  .contact-list {
    position: absolute;
    left: 64px;
    bottom: 64px;
    list-style: none;
    display: flex;
    flex-direction: column;
    gap: 10px;
    font-family: "Inter", sans-serif;
    font-size: 21px;
    color: var(--gold);
  }
  .contact-list li {
    display: flex;
    align-items: center;
    gap: 12px;
  }
  .contact-icon {
    width: 22px;
    height: 22px;
    flex: none;
  }
  .card--back .brand-mark {
    position: absolute;
    right: 56px;
    bottom: 58px;
    gap: 12px;
  }
  .card--back .brand-mark__square {
    width: 22px;
    height: 22px;
  }
  .card--back .brand-mark__name {
    font-size: 24px;
  }
</style>
</head>
<body>
  <main class="canvas">
    <section class="card card--front" aria-label="Card front">
      <div class="brand-mark">
        <span class="brand-mark__square" aria-hidden="true"></span>
        <span class="brand-mark__name">Marlow Tow and Lease</span>
      </div>
      <p class="company-line">THE MARLOW TOW AND LEASE</p>
    </section>

    <section class="card card--back" aria-label="Card back">
      <h1 class="holder-name">Dale K</h1>
      <ul class="contact-list">
        <li>
          <svg class="contact-icon" viewBox="0 0 22 22" aria-hidden="true">
            <circle cx="11" cy="11" r="11" fill="#c9982f"/>
            <path d="M8 6.5c-.8.4-1.4 1.4-.9 2.8.8 2.3 2.4 4 4.7 5 1.3.6 2.4 0 2.8-.8l-1.6-1.5-1.2.7c-1-.5-1.8-1.3-2.3-2.3l.7-1.2z" fill="#1f2021"/>
          </svg>
          <span>475 286 9014</span>
        </li>
        <li>
          <svg class="contact-icon" viewBox="0 0 22 22" aria-hidden="true">
            <circle cx="11" cy="11" r="11" fill="#c9982f"/>
            <rect x="5.5" y="7" width="11" height="8" fill="none" stroke="#1f2021" stroke-width="1.5"/>
            <path d="M5.5 7.5 11 11.5 16.5 7.5" fill="none" stroke="#1f2021" stroke-width="1.5"/>
          </svg>
          <span>marlowtow@fennmail.test</span>
        </li>
      </ul>
      <div class="brand-mark">
        <span class="brand-mark__square" aria-hidden="true"></span>
        <span class="brand-mark__name">Marlow Tow and Lease</span>
      </div>
    </section>
  </main>
</body>
</html>
```